SEHLAN REAL ESTATE
شركة السهلان العقارية
Creative Brief
Simple
FAISAL ALQUDRANI
Real Estate Consultant & Developer
SAUDI ARABIA.JEDDAH
f_alqudrani@mailvesta.com
THE LOGO
Yasahiro17 Yasahiro17
YADESIGN YADESIGN

```html
<!DOCTYPE html>
<html lang="en">
<head>
<meta charset="utf-8">
<title>Sehlan Real Estate – Business Card</title>
<link href="https://fonts.googleapis.com/css2?family=Cinzel:wght@400;500&family=Cairo:wght@500&display=swap" rel="stylesheet">
<style>
  :root {
    --backdrop: #f2f2f2;
    --card: #ffffff;
    --brand-blue: #2f7fc1;
    --ink: #3b4049;
    --muted: #6b7078;
  }
  html, body {
    margin: 0;
    padding: 0;
    width: 1200px;
    height: 871px;
    overflow: hidden;
    background: var(--backdrop);
  }
  .canvas {
    position: relative;
    width: 1200px;
    height: 871px;
  }
  .card {
    position: absolute;
    left: 312px;
    width: 576px;
    height: 340px;
    background: var(--card);
  }
  .card--front { top: 84px; }
  .card--back { top: 466px; }

  .brand {
    position: absolute;
    display: flex;
    align-items: center;
  }
  .brand__mark {
    background: var(--brand-blue);
    flex: none;
  }
  .brand__text {
    display: flex;
    flex-direction: column;
    align-items: stretch;
  }
  .brand__name {
    font-family: "Cinzel", serif;
    font-weight: 500;
    color: var(--ink);
    line-height: 1;
    letter-spacing: 0.02em;
  }
  .brand__tagline {
    display: flex;
    align-items: center;
    gap: 6px;
    font-family: "Cinzel", serif;
    color: var(--ink);
    letter-spacing: 0.18em;
    line-height: 1;
  }
  .brand__tagline::before,
  .brand__tagline::after {
    content: "";
    flex: 1;
    height: 1px;
    background: var(--ink);
  }
  .brand__arabic {
    font-family: "Cairo", sans-serif;
    font-weight: 500;
    color: var(--ink);
    line-height: 1.1;
    text-align: right;
    direction: rtl;
  }

  /* front card */
  .card--front .brand { left: 52px; top: 46px; gap: 18px; }
  .card--front .brand__mark { width: 30px; height: 30px; }
  .card--front .brand__name { font-size: 38px; }
  .card--front .brand__tagline { font-size: 11px; margin-top: 6px; }
  .card--front .brand__arabic { font-size: 26px; margin-top: 2px; }

  .person {
    position: absolute;
    left: 67px;
    top: 172px;
  }
  .person__name {
    font-family: "Cinzel", serif;
    font-size: 17px;
    color: var(--ink);
    margin: 0;
    letter-spacing: 0.02em;
  }
  .person__role {
    font-family: "Cinzel", serif;
    font-size: 9px;
    color: var(--brand-blue);
    margin: 3px 0 0;
    letter-spacing: 0.04em;
  }
  .contact {
    position: absolute;
    left: 67px;
    top: 240px;
    margin: 0;
    padding: 0;
    list-style: none;
    font-family: "Cinzel", serif;
    font-size: 9.5px;
    color: var(--muted);
    line-height: 18px;
    letter-spacing: 0.03em;
  }

  /* back card */
  .card--back .brand { left: 108px; top: 108px; gap: 26px; }
  .card--back .brand__mark { width: 44px; height: 44px; }
  .card--back .brand__name { font-size: 50px; }
  .card--back .brand__tagline { font-size: 14px; margin-top: 8px; }
  .card--back .brand__arabic { font-size: 34px; margin-top: 2px; }
</style>
</head>
<body>
<main class="canvas">
  <section class="card card--front" aria-label="Business card front">
    <div class="brand">
      <span class="brand__mark" aria-hidden="true"></span>
      <div class="brand__text">
        <span class="brand__name">SEHLAN</span>
        <span class="brand__tagline">REAL ESTATE</span>
        <span class="brand__arabic">شركة السهلان العقارية</span>
      </div>
    </div>
    <div class="person">
      <p class="person__name">FAISAL ALQUDRANI</p>
      <p class="person__role">Real Estate Consultant &amp; Developer</p>
    </div>
    <ul class="contact">
      <li>SAUDI ARABIA.JEDDAH</li>
      <li>+966512340987</li>
      <li>F_ALQUDRANI@MAILVESTA.COM</li>
    </ul>
  </section>

  <section class="card card--back" aria-label="Business card back">
    <div class="brand">
      <span class="brand__mark" aria-hidden="true"></span>
      <div class="brand__text">
        <span class="brand__name">SEHLAN</span>
        <span class="brand__tagline">REAL ESTATE</span>
        <span class="brand__arabic">شركة السهلان العقارية</span>
      </div>
    </div>
  </section>
</main>
</body>
</html>
```